Freelance business trainer needs a new business card

My business is called Tbrite. I provide training in the workplace on management, coaching and mentoring, and customer service topics for a variety of businesses, colleges and private training providers, and teach on management programs. I need a professional but eye catching business card. Business colours grey and orange. My name Linda Marchbank; Tel 07853 416207; email lmarchbank@tbrite.co.uk; website www.tbrite.co.uk.
Happy to have some sort of logo on front and details on back or all on one side
Target Market(s)
SME businesses and colleges - workshops i run are for adults in the workplace
Industry/Entity Type
Training
Look and feel

```html
<!DOCTYPE html>
<html lang="en">
<head>
<meta charset="utf-8">
<title>Tbrite business card</title>
<link rel="stylesheet" href="https://fonts.googleapis.com/css2?family=Ubuntu:wght@400;500;700&display=swap">
<style>
  :root {
    --backdrop: #353535;
    --card-grey: #424242;
    --brand-orange: #f7901e;
    --text-white: #ffffff;
    --icon-light: #e6e6e6;
    --mark-dark: #3f3f3f;
  }
  * { box-sizing: border-box; margin: 0; padding: 0; }
  html, body {
    width: 1200px;
    height: 750px;
    overflow: hidden;
  }
  body {
    position: relative;
    background: var(--backdrop);
    font-family: "Ubuntu", sans-serif;
  }
  .card {
    position: absolute;
    top: 214px;
    width: 494px;
    height: 286px;
    border-radius: 14px;
    background: var(--card-grey);
    overflow: hidden;
  }
  .card--front { left: 92px; }
  .card--back { left: 620px; }

  /* front */
  .front-brand {
    position: absolute;
    left: 0; right: 0;
    top: 110px;
    display: flex;
    align-items: center;
    justify-content: center;
    gap: 12px;
  }
  .front-brand__square {
    width: 26px;
    height: 26px;
    background: var(--text-white);
  }
  .front-brand__name {
    font-size: 46px;
    font-weight: 500;
    color: var(--brand-orange);
    line-height: 1;
  }
  .front-web {
    position: absolute;
    left: 0; right: 0;
    top: 257px;
    text-align: center;
    font-size: 14px;
    font-weight: 700;
    color: var(--brand-orange);
    letter-spacing: 0.2px;
  }

  /* back */
  .brand-band {
    position: absolute;
    left: 0; top: 0;
    width: 115px;
    height: 100%;
    background: var(--brand-orange);
  }
  .brand-band__name {
    position: absolute;
    left: 0; right: 0;
    top: 190px;
    text-align: center;
    font-size: 30px;
    font-weight: 500;
    color: var(--mark-dark);
    line-height: 1;
  }
  .person {
    position: absolute;
    left: 170px;
    top: 98px;
  }
  .person__name {
    font-size: 15px;
    font-weight: 700;
    color: var(--text-white);
    letter-spacing: 0.2px;
  }
  .person__role {
    margin-top: 5px;
    font-size: 15px;
    color: var(--brand-orange);
  }
  .contacts {
    position: absolute;
    left: 167px;
    top: 197px;
    list-style: none;
  }
  .contacts__item {
    display: flex;
    align-items: center;
    gap: 6px;
    height: 21px;
    font-size: 15px;
    color: var(--brand-orange);
  }
  .contacts__icon {
    width: 13px;
    height: 13px;
    flex: none;
    fill: var(--icon-light);
  }
</style>
</head>
<body>
  <section class="card card--front">
    <div class="front-brand">
      <span class="front-brand__square"></span>
      <span class="front-brand__name">Tbrite</span>
    </div>
    <p class="front-web">www.tbrite.co.uk.</p>
  </section>

  <section class="card card--back">
    <div class="brand-band">
      <span class="brand-band__name">Tbrite</span>
    </div>
    <div class="person">
      <p class="person__name">Linda Marchbank</p>
      <p class="person__role">Owner</p>
    </div>
    <ul class="contacts">
      <li class="contacts__item">
        <svg class="contacts__icon" viewBox="0 0 16 16" aria-hidden="true">
          <path d="M1 5c0-2 3-3 7-3s7 1 7 3v1h-4V4.5H5V6H1z"/>
          <path d="M3 8l2-2h6l2 2v6H3zM8 9a2 2 0 1 0 0 4 2 2 0 0 0 0-4z"/>
        </svg>
        <span>07853 416207</span>
      </li>
      <li class="contacts__item">
        <svg class="contacts__icon" viewBox="0 0 16 16" aria-hidden="true">
          <path d="M1 3h14v1.2L8 9 1 4.2z"/>
          <path d="M1 5.6l7 4.8 7-4.8V13H1z"/>
        </svg>
        <span>lmarchbank@tbrite.co.uk</span>
      </li>
      <li class="contacts__item">
        <svg class="contacts__icon" viewBox="0 0 16 16" aria-hidden="true">
          <path fill-rule="evenodd" d="M8 1a7 7 0 1 1 0 14A7 7 0 0 1 8 1zm-.7 1.6C6.3 3.7 5.7 5.2 5.6 7.3h1.7zm1.4 0v4.7h1.7c-.1-2.1-.7-3.6-1.7-4.7zM2.6 7.3h1.9c.1-1.7.5-3.1 1.2-4.1A5.6 5.6 0 0 0 2.6 7.3zm8.9 0h1.9a5.6 5.6 0 0 0-3.1-4.1c.7 1 1.1 2.4 1.2 4.1zM2.6 8.7a5.6 5.6 0 0 0 3.1 4.1c-.7-1-1.1-2.4-1.2-4.1zm3 0c.1 2.1.7 3.6 1.7 4.7V8.7zm3.1 0v4.7c1-1.1 1.6-2.6 1.7-4.7zm2.8 0c-.1 1.7-.5 3.1-1.2 4.1a5.6 5.6 0 0 0 3.1-4.1z"/>
        </svg>
        <span>www.tbrite.co.uk.</span>
      </li>
    </ul>
  </section>
</body>
</html>
```